Business card needed for home based pen making business.

I'm after a business card that's a bit more than an off the shelf card. I do like the idea of a card split horizontal with different colours used. A third colour is to be used for the business name and if need a forth for the other details.

I don't have a logo and will pay extra for one ($150 extra). I mainly make pens and seam rippers (stitch unpicks). The logo may be used for a website in future, as will the colours so please provide the colour codes and font type.

I'd like the business name in an easy to read script font at the top (with logo if you have one) and the other details to the bottom left hand side. I'll leave it up to you to match the script to the font used for the other details.

I'd like to keep a triangular balance to the card so something like a siloet of pot containing pens on the bottom right could be used to balance it out. There my ideas I want to see your.

Business name: Quill & Co
Email address: quillandco@mailbox-example.net
Contact: Trevor
Phone: 0412 555 874
No address is to be used on card.

Target Market(s)

Wide variety of people visiting craft markets. Age range 30+.

Industry/Entity Type

Business

Contact Information for Business Card

Quill & Co

Font styles to use
Script

Colors
f0ecf4
3277b5
3176b5

Requirements
Must have
• Contact: Trevor
• Phone: 0412 555 874
• Email address: quillandco@mailbox-example.net
Nice to have
• An icon and/or graphics depicting pens and seam rippers..
Should not have
• I don't want icon/ graphic to be a crossed pen and seam ripper.

```html
<!DOCTYPE html>
<html lang="en">
<head>
<meta charset="utf-8">
<title>Quill &amp; Co — Business Card</title>
<link rel="stylesheet" href="https://fonts.googleapis.com/css2?family=Berkshire+Swash&family=Libre+Baskerville:ital@1&display=swap">
<style>
  :root {
    --stage: #e4e4e6;
    --card: #f0ecf4;
    --brand-blue: #3277b5;
    --ink: #111111;
    --rule: #333333;
    --wood-light: #c9a66b;
    --wood-dark: #8a6330;
  }
  * { margin: 0; padding: 0; box-sizing: border-box; }
  html, body {
    width: 1200px;
    height: 902px;
    overflow: hidden;
    background: var(--stage);
  }
  .business-card {
    position: absolute;
    left: 60px;
    top: 143px;
    width: 1080px;
    height: 616px;
    background: var(--card);
    box-shadow: 0 6px 18px rgba(0, 0, 0, 0.12);
  }
  .business-name {
    position: absolute;
    left: 40px;
    top: 52px;
    font-family: "Berkshire Swash", cursive;
    font-size: 66px;
    line-height: 1;
    color: var(--brand-blue);
    white-space: nowrap;
  }
  .product-photo {
    position: absolute;
    left: 19px;
    top: 300px;
    width: 560px;
    height: 200px;
  }
  .divider {
    position: absolute;
    left: 612px;
    top: 44px;
    width: 2px;
    height: 528px;
    background: var(--rule);
  }
  .contact-name {
    position: absolute;
    left: 649px;
    top: 350px;
    font-family: "Berkshire Swash", cursive;
    font-size: 48px;
    line-height: 1;
    color: var(--brand-blue);
  }
  .contact-details {
    position: absolute;
    left: 649px;
    top: 466px;
    font-family: "Libre Baskerville", serif;
    font-style: italic;
    font-size: 27px;
    line-height: 47px;
    color: var(--ink);
    list-style: none;
    white-space: nowrap;
  }
</style>
</head>
<body>
  <article class="business-card">
    <h1 class="business-name">Quill &amp; Co</h1>

    <svg class="product-photo" role="img" aria-label="Photo of a handmade seam ripper with a turned timber handle and brass fittings" viewBox="0 0 560 200" xmlns="http://www.w3.org/2000/svg">
      <defs>
        <linearGradient id="wood-tone" x1="0" y1="0" x2="1" y2="1">
          <stop offset="0" stop-color="var(--wood-light)" stop-opacity="0.55"/>
          <stop offset="1" stop-color="var(--wood-dark)" stop-opacity="0.55"/>
        </linearGradient>
      </defs>
      <rect width="560" height="200" fill="url(#wood-tone)"/>
    </svg>

    <div class="divider" aria-hidden="true"></div>

    <p class="contact-name">Trevor</p>
    <ul class="contact-details">
      <li class="contact-phone">0412 555 874</li>
      <li class="contact-email">quillandco@mailbox-example.net</li>
    </ul>
  </article>
</body>
</html>
```